Business card - Brio Margin - size 85 mm * 55 mm

We need new business cards. Design must fit with our vision of the firm. You find in the attached file our logo and a short description of our firm (mission, vision, value, business and so on).

Target Market(s)

Consulting firm in performance improvement

Industry/Entity Type

Management Consulting

Contact Information for Business Card

SIZE
85 mm * 55 mm
INFORMATIONS
name surname
role position
telephone number
email address

Requirements
Must have
• the brand must APPEAR for the rest Would we like to have something sleek, inspired to a "just right" approach
Should not have
• Please avoid the black color as background

```html
<!DOCTYPE html>
<html lang="en">
<head>
<meta charset="utf-8">
<title>Brio Margin – Business Card</title>
<link rel="stylesheet" href="https://fonts.googleapis.com/css2?family=Source+Sans+3:wght@400;600&display=swap">
<style>
  :root {
    --stage: #3b3b3b;
    --card-white: #ffffff;
    --brand-orange: #ff6600;
    --accent-sage: #a9c9a4;
    --text-light: #ffffff;
    --font-main: "Source Sans 3", Arial, sans-serif;
  }
  * { margin: 0; padding: 0; box-sizing: border-box; }
  html, body {
    width: 1105px;
    height: 1200px;
    overflow: hidden;
    background: var(--stage);
    font-family: var(--font-main);
  }
  .card {
    position: absolute;
    left: 217px;
    width: 688px;
    height: 445px;
    overflow: hidden;
    box-shadow: 0 4px 10px rgba(0,0,0,0.35);
  }
  .card--front { top: 135px; background: var(--card-white); }
  .card--back  { top: 627px; background: var(--brand-orange); }

  .brand {
    position: absolute;
    left: 0; right: 0;
    display: flex;
    flex-direction: column;
    align-items: center;
  }
  .brand__mark {
    border-radius: 50%;
    border-style: solid;
  }
  .brand__name {
    font-weight: 400;
    text-transform: uppercase;
    white-space: nowrap;
  }
  .card--front .brand { top: 44px; }
  .card--front .brand__mark {
    width: 130px; height: 130px;
    border-width: 5px;
    border-color: var(--brand-orange);
  }
  .card--front .brand__name {
    margin-top: 24px;
    font-size: 23px;
    letter-spacing: 0.42em;
    margin-right: -0.42em;
    color: var(--brand-orange);
  }
  .card--back .brand { top: 94px; }
  .card--back .brand__mark {
    width: 160px; height: 160px;
    border-width: 7px;
    border-color: var(--text-light);
  }
  .card--back .brand__name {
    margin-top: 30px;
    font-size: 31px;
    letter-spacing: 0.42em;
    margin-right: -0.42em;
    color: var(--text-light);
  }

  .front-band {
    position: absolute;
    left: 0; top: 0;
    width: 688px; height: 445px;
  }
  .contact {
    position: absolute;
    left: 0; right: 0;
    top: 318px;
    text-align: center;
    color: var(--text-light);
  }
  .contact__name { font-size: 22px; font-weight: 600; }
  .contact__role { font-size: 18px; font-weight: 400; }
  .contact__lines {
    margin-top: 8px;
    font-size: 17px;
  }
  .contact__label { font-weight: 600; }
  .contact__gap { display: inline-block; width: 12px; }
  .contact__web {
    margin-top: 6px;
    font-size: 17px;
    font-weight: 600;
    letter-spacing: 0.32em;
    margin-right: -0.32em;
  }
</style>
</head>
<body>
  <section class="card card--front">
    <svg class="front-band" viewBox="0 0 688 445" aria-hidden="true">
      <path d="M0 307 Q344 252 688 307" fill="none" stroke="var(--accent-sage)" stroke-width="6"/>
      <path d="M0 313 Q344 260 688 313 L688 445 L0 445 Z" fill="var(--brand-orange)"/>
    </svg>
    <div class="brand">
      <div class="brand__mark"></div>
      <div class="brand__name">Brio Margin</div>
    </div>
    <div class="contact">
      <div><span class="contact__name">Tomas Reyl -</span> <span class="contact__role">President</span></div>
      <div class="contact__lines">
        <span class="contact__label">P :</span> 555 0142 7781<span class="contact__gap"></span><span class="contact__label">E :</span> name@briomargin.com
      </div>
      <div class="contact__web">www.briomargin.com</div>
    </div>
  </section>

  <section class="card card--back">
    <div class="brand">
      <div class="brand__mark"></div>
      <div class="brand__name">Brio Margin</div>
    </div>
  </section>
</body>
</html>
```